RT Pemberly Electric Yard Sign

Looking to have a yard sign designed that we can place at projects we are working on. Most likely will be 18" H x 24" W but flexible that we can increase the size if necessary. It should include our logo, our phone # 609-555-0147, website rtpemberlyelectric-example.com and slogan, built on integrity, driven by excellence. Colors should match our brand.

```html
<!DOCTYPE html>
<html lang="en">
<head>
<meta charset="utf-8">
<title>RT Pemberly Electric Yard Sign</title>
<link rel="stylesheet" href="https://fonts.googleapis.com/css2?family=Saira+Semi+Condensed:wght@400;600;700;800&display=swap">
<style>
  :root {
    --brand-red: #e31f13;
    --brand-navy: #0a3468;
    --quote-salmon: #f4a386;
    --sign-white: #ffffff;
    --backdrop: #eceef1;
  }
  * { margin: 0; padding: 0; box-sizing: border-box; }
  html, body { width: 1200px; height: 659px; overflow: hidden; }
  body {
    background: var(--backdrop);
    font-family: "Saira Semi Condensed", "Arial Narrow", sans-serif;
    display: flex; justify-content: center; align-items: center;
  }
  .yard-sign {
    position: relative;
    width: 494px; height: 659px;
    background: var(--sign-white);
    overflow: hidden;
  }
  .sign-waves { position: absolute; inset: 0; width: 100%; height: 100%; }
  .slogan-block {
    position: absolute; left: 0; right: 0; top: 40px;
    color: var(--sign-white); text-align: center;
  }
  .quote-rule {
    display: flex; align-items: center; justify-content: center; gap: 10px;
    height: 40px;
  }
  .quote-rule .rule { width: 128px; height: 2px; background: var(--sign-white); }
  .quote-rule.closing .rule { width: 165px; }
  .quote-mark {
    color: var(--quote-salmon); font-weight: 800; font-size: 72px;
    line-height: 1; height: 40px; font-family: Georgia, serif;
  }
  .quote-rule.opening .quote-mark { transform: translateY(6px); }
  .quote-rule.closing .quote-mark { transform: translateY(14px); }
  .slogan-line { display: block; line-height: 1; letter-spacing: 0.2px; }
  .slogan-line.strong { font-weight: 700; font-size: 46px; margin-top: 6px; }
  .slogan-line.light { font-weight: 400; font-size: 47px; margin-top: 2px; }
  .brand-name {
    position: absolute; left: 0; right: 0; top: 418px;
    display: flex; justify-content: center; align-items: center; gap: 10px;
    color: var(--brand-navy); font-weight: 700; font-size: 40px; line-height: 1;
  }
  .brand-dot { width: 16px; height: 16px; border-radius: 50%; background: var(--brand-red); }
  .phone-number {
    position: absolute; left: 0; right: 0; top: 526px;
    text-align: center; color: var(--brand-navy);
    font-weight: 800; font-size: 64px; line-height: 1; letter-spacing: 0.5px;
  }
  .web-address {
    position: absolute; left: 0; right: 0; top: 594px;
    display: flex; justify-content: center; align-items: center; gap: 8px;
    color: var(--brand-red); font-weight: 600; font-size: 24px; line-height: 1;
  }
  .web-address .dash { width: 26px; height: 3px; background: var(--brand-red); }
</style>
</head>
<body>
  <main class="yard-sign">
    <svg class="sign-waves" viewBox="0 0 1040 1388" preserveAspectRatio="none" aria-hidden="true">
      <path fill="var(--brand-navy)" d="M0 0 H1040 V650 C950 570 800 580 640 620 C450 680 250 770 0 690 Z"/>
      <path fill="var(--brand-red)" d="M0 0 H1040 V560 C900 540 760 555 600 605 C420 660 200 665 0 560 Z"/>
      <path fill="var(--sign-white)" d="M380 650 C560 610 720 560 880 548 C780 560 700 585 600 612 C520 630 450 642 380 650 Z"/>
    </svg>

    <section class="slogan-block">
      <div class="quote-rule opening"><span class="rule"></span><span class="quote-mark">&ldquo;</span><span class="rule"></span></div>
      <h1>
        <span class="slogan-line strong">Built On Integrity,</span>
        <span class="slogan-line light">Driven By Excellence</span>
      </h1>
      <div class="quote-rule closing"><span class="rule"></span><span class="quote-mark">&rdquo;</span><span class="rule"></span></div>
    </section>

    <div class="brand-name"><span class="brand-dot"></span><span>RT Pemberly Electric</span></div>
    <p class="phone-number">609-555-0147</p>
    <p class="web-address"><span class="dash"></span><span>rtpemberlyelectric-example.com</span><span class="dash"></span></p>
  </main>
</body>
</html>
```